WordPress design needed for scientist

Hi! I am a female scientist (36 years old) in the field of marine science and biotechnology. I need a clean, engaging, modern WordPress website design. Not just a blog, but a site that shows pictures of my research and topics, can host PDFs of my research publications, and can have my Twitterfeed (@mirabelleskov) and YouTube videos embedded. Something a bit like this: http://www.varnholt.org.uk/ but with my content, and a more engaging design, like the template "PLUME"

My current webprofile from the University of Kestrelmoor is here: http://www.uok.no/personer/Mirabelle.Ruth.Skovlund , but I need something that is more than this, that can inspire grant evaluators to pick me, and a website that shows the best sides of me and my research. I attach some representative pictures of me and my research that I would like to be used/incorporated in the webdesign.

Target Market(s)

other scientists, journalists, media, interested members of the public

Industry/Entity Type

Biotechnology

Font styles to use
Sans Serif

Requirements
Must have
• YouTube video embedding of these videos:
• https://www.vidstreamo.com/watch?v=7KpQzT2mWx4
• https://www.vidstreamo.com/watch?v=rB3nYhLcPe8
• https://www.vidstreamo.com/watch?v=gT9dWuKsZa2
• Prezi Presentations embedded: https://slidovo.com/user/mirabelleskov/

```html
<!DOCTYPE html>
<html lang="en">
<head>
<meta charset="utf-8">
<title>Mirabelle R. Skovlund</title>
<link href="https://fonts.googleapis.com/css2?family=Antonio:wght@400&family=Oswald:wght@400&family=Lato:wght@400;700&display=swap" rel="stylesheet">
<style>
:root{
  --blue:#2fb4f3;
  --ink:#222;
  --text:#666;
  --black:#000;
  --rule:#cfcfcf;
  --white:#fff;
}
*{box-sizing:border-box;margin:0;padding:0}
html,body{width:808px;height:1200px;overflow:hidden;background:var(--white)}
body{position:relative;font-family:'Lato',sans-serif;color:var(--text)}
.abs{position:absolute}
h1,h2,h3{font-weight:400}

.topbar{left:0;top:0;width:808px;height:40px;background:var(--black);border-top:3px solid var(--blue)}
.social{left:37px;top:7px;display:flex;gap:7px}
.social span{width:25px;height:25px;border-radius:50%;border:1.5px solid #ddd;display:block}
.social span.on{background:var(--blue);border-color:var(--blue)}
.phone{left:654px;top:0;width:124px;height:34px;background:var(--blue);border-radius:0 0 4px 4px;color:var(--white);font-size:14px;display:flex;align-items:center;justify-content:center;gap:7px}

.logo{left:37px;top:63px;font-family:'Antonio',sans-serif;font-size:33px;color:var(--blue);line-height:1;white-space:nowrap}
.nav{left:350px;top:64px;display:flex;align-items:center;font-family:'Oswald',sans-serif;font-size:13px;color:#333;text-transform:uppercase;white-space:nowrap}
.nav a{color:inherit;text-decoration:none;height:38px;line-height:38px;padding:0 14px}
.nav a.current{background:var(--blue);color:var(--white);border-radius:2px}

.hero{left:0;top:125px;width:808px;height:359px;background:linear-gradient(100deg,#1a5fc8 0%,#2f86e6 35%,#8fb8e6 60%,#3c7ed8 85%,#1e62cc 100%)}
.hero-card{left:37px;top:201px;width:375px;height:231px;background:rgba(10,14,20,.85)}
.hero-card h1{position:absolute;left:21px;top:24px;font-family:'Antonio',sans-serif;font-size:34px;line-height:45px;color:var(--white);text-transform:uppercase;white-space:nowrap}
.hero-card p{position:absolute;left:24px;top:116px;width:340px;font-size:13px;line-height:22px;color:#eee}
.btn{display:inline-block;background:var(--blue);color:var(--white);font-weight:700;font-size:12px;padding:0 12px;height:29px;line-height:29px;border-radius:1px;white-space:nowrap}
.hero-card .btn{position:absolute;left:23px;top:179px}

.section-title{left:0;width:808px;text-align:center;font-family:'Oswald',sans-serif;font-size:19px;color:var(--ink);text-transform:uppercase;white-space:nowrap}
.section-title em{font-style:normal;color:var(--blue)}
.divider{left:352px;width:112px;height:3px;display:flex;gap:3px}
.divider i{display:block;height:3px;background:var(--rule);width:45px}
.divider i.mid{background:var(--blue);width:16px}

.about-h{left:37px;top:569px;font-family:'Oswald',sans-serif;font-size:15px;color:var(--ink);text-transform:uppercase;white-space:nowrap}
.about-rule{left:37px;top:597px;width:179px;height:4px;border-top:1px solid #333;border-bottom:1px solid #333}
.about-p{left:37px;top:610px;width:372px;font-size:11.5px;line-height:19.2px}
.about-btn{left:37px;top:750px}

.video{left:428px;top:573px;width:350px;height:207px;border-radius:4px;background:linear-gradient(120deg,#8a8c78 0%,#d9d8cd 35%,#ecebe3 60%,#b9b6a4 85%,#8d3a2c 100%);overflow:hidden}
.player{left:17px;top:158px;width:318px;height:30px}

.cards{left:37px;top:871px;display:flex;gap:22px}
.card{width:232px}
.card .pic{height:139px;border-radius:3px}
.card h3{margin-top:10px;font-family:'Oswald',sans-serif;font-size:14.5px;color:var(--ink);text-transform:uppercase;white-space:nowrap}
.card .sep{position:relative;margin:6px 0 10px;height:5px;width:186px}
.card .sep:before{content:"";position:absolute;left:0;right:0;top:2px;border-top:1px dotted #bbb}
.card .sep:after{content:"";position:absolute;left:0;top:0;width:5px;height:5px;border-radius:50%;background:var(--blue)}
.card p{font-size:11.5px;line-height:16px;letter-spacing:-.1px}

.footer{left:0;top:1146px;width:808px;height:54px;background:var(--blue);text-align:center;color:var(--white)}
.footer nav{padding-top:10px;font-size:12px}
.footer nav a{color:var(--white);text-decoration:none}
.footer nav a.current{color:#111}
.footer nav b{font-weight:400;margin:0 9px}
.footer small{display:block;margin-top:6px;font-size:10px;color:#eaf7ff}
</style>
</head>
<body>

<header>
  <div class="abs topbar"></div>
  <div class="abs social" aria-label="Social links">
    <span class="on"></span><span></span><span></span><span></span><span></span><span></span>
  </div>
  <div class="abs phone">
    <svg width="14" height="14" viewBox="0 0 24 24" aria-hidden="true"><path fill="#fff" d="M6.6 10.8a15.1 15.1 0 0 0 6.6 6.6l2.2-2.2c.3-.3.7-.4 1-.2 1.1.4 2.3.6 3.6.6.6 0 1 .4 1 1V20c0 .6-.4 1-1 1C10.6 21 3 13.4 3 4c0-.6.4-1 1-1h3.5c.6 0 1 .4 1 1 0 1.3.2 2.5.6 3.6.1.3 0 .7-.2 1z"/></svg>
    123- 456-7890
  </div>
  <div class="abs logo">Mirabelle R. Skovlund</div>
  <nav class="abs nav">
    <a class="current">Home</a><a>Publication</a><a>Bio</a><a>Projects</a><a>Vision</a><a>Contact</a>
  </nav>
</header>

<section>
  <div class="abs hero" role="img" aria-label="Photo of the scientist speaking with a headset microphone in front of a research vessel, blue-toned"></div>
  <div class="abs hero-card">
    <h1>Lorem ipsum dolor sitam<br>consec teturadipiscingel</h1>
    <p>Maecenas Suscipit Tincidunt Posuereullam Iaculis Massa Mauris anisiid diamcurs dictumurabitur ornarelectus....</p>
    <span class="btn">Learn More</span>
  </div>
</section>

<section>
  <h2 class="abs section-title" style="top:514px">Welcome to <em>Mirabelle R. Skovlund</em></h2>
  <div class="abs divider" style="top:548px"><i></i><i class="mid"></i><i></i></div>

  <h3 class="abs about-h">About us Mirabelle R. Skovlund</h3>
  <div class="abs about-rule"></div>
  <p class="abs about-p">Lorem ipsum dolor sit amet, consectetur adipiscinglit. Donec nec dignis im lorem. Vestibulum lesuada ac auctor vitae, mollis tempus dolor aese nt tincidunt felis eget dui consequat consectetur.orbi suscipit justo tellus, eu dictum metus ultrices nec. Suspendisse at ipsum suscipit nunc placerat porttitor. Integer eget lobortis nulla. Etiam scelerisque neque et cursus vehicula. Sed sed lobortis ante, sed commodo eros. Fusce eget dictum tellus.  sum suscipit nunc placerat porttitor....</p>
  <span class="abs btn about-btn">Learn More</span>

  <div class="abs video" role="img" aria-label="Video still of a hand pointing at a laboratory poster about fertilisation tests">
    <svg class="abs player" viewBox="0 0 318 30" aria-hidden="true">
      <rect x="0" y="0" width="48" height="30" rx="3" fill="#2b2b2b"/>
      <path d="M19 8 L31 15 L19 22Z" fill="#fff"/>
      <rect x="53" y="3" width="265" height="24" fill="#2b2b2b"/>
      <rect x="63" y="11" width="146" height="7" fill="#555"/>
      <rect x="63" y="11" width="125" height="7" fill="#999"/>
      <rect x="63" y="11" width="44" height="7" fill="#2fb4f3"/>
      <g fill="#2fb4f3"><rect x="234" y="11" width="2" height="8"/><rect x="238" y="11" width="2" height="8"/><rect x="242" y="11" width="2" height="8"/><rect x="246" y="11" width="2" height="8"/><rect x="250" y="11" width="2" height="8"/></g>
      <text x="256" y="19" font-family="Lato,sans-serif" font-weight="700" font-style="italic" font-size="10" fill="#2fb4f3">HD</text>
      <path d="M287 10h3v1h-2v2h-1zM294 10h3v3h-1v-2h-2zM287 17h1v2h2v1h-3zM296 17h1v3h-3v-1h2z" fill="#fff"/>
    </svg>
    <svg class="abs" style="left:100px;top:141px" width="28" height="14" viewBox="0 0 28 14" aria-hidden="true">
      <rect width="28" height="11" fill="#fff"/><path d="M11 11h6l-3 3z" fill="#fff"/>
      <text x="14" y="8.5" text-anchor="middle" font-family="Lato,sans-serif" font-size="8" fill="#333">02:49</text>
    </svg>
  </div>
</section>

<section>
  <h2 class="abs section-title" style="top:812px">Our <em>Case Study</em></h2>
  <div class="abs divider" style="top:845px"><i></i><i class="mid"></i><i></i></div>

  <div class="abs cards">
    <article class="card">
      <div class="pic" role="img" aria-label="Workshop participants working on laptops around a table" style="background:linear-gradient(135deg,#6b5a4a,#b89a7a 40%,#3a3230 75%,#8a7060)"></div>
      <h3>Vestibulum pulvinar metus</h3>
      <div class="sep"></div>
      <p>Lorem ipsum dolor sit amet, consectetur dipis cinglit. Donec nec dignissim lorem. Vestibulum lesuada ac auctor vitae, mollis</p>
    </article>
    <article class="card">
      <div class="pic" role="img" aria-label="Seminar room with participants seated at tables facing a presenter" style="background:linear-gradient(160deg,#d8d6d0,#9a9890 45%,#4a4844 80%,#6a6660)"></div>
      <h3>Nullam pretium hendrerit</h3>
      <div class="sep"></div>
      <p>Lorem ipsum dolor sit amet, consecteturadi piscinglit. Donec nec dignissim loremesti ulum lesuada ac auctor vitae, mollis tempus dolor.</p>
    </article>
    <article class="card">
      <div class="pic" role="img" aria-label="Group discussion around a meeting table" style="background:linear-gradient(140deg,#8a8f96,#c9c6c0 40%,#6a6460 70%,#b8b0a6)"></div>
      <h3>Nullam hendrerit efficitur</h3>
      <div class="sep"></div>
      <p>Lorem ipsum dolor sit amet, consectetur ipisi nglit. Donec nec dignissim lorem. Vestibulum lesuada ac au ctor vitae, mollis tempus dolor</p>
    </article>
  </div>
</section>

<footer class="abs footer">
  <nav><a class="current">Home</a><b>/</b><a>Publication</a><b>/</b><a>Bio</a><b>/</b><a>Projects</a><b>/</b><a>Vision</a><b>/</b><a>Contact</a></nav>
  <small>©2016Mirabelle R. Skovlund.&nbsp; | &nbsp;All Rights Resverd.</small>
</footer>

</body>
</html>
```